Simple Business Card Design

Professional/clean business card with custom logo included in layout.

Target Market(s)

N/A

Industry/Entity Type

Business

Contact Information for Business Card

Name: Marlene Voskin, PT; NV Medicaid Provider; Phone: (775) 918-2246; Toll-free phone: (877) 461-5092; email: mar@tidewellbranchsystemsltd.example

Font styles to use
Serif
Decorative
Script

Requirements
Must have
• See "details" above.
Nice to have
• Would be interested to see dark vs. light/grayscale backgrounds that accentuate/contrast the logo colors. (I.e. dark navy background w/ white or grey text, etc.)

```html
<!DOCTYPE html>
<html lang="en">
<head>
<meta charset="utf-8">
<title>Tidewell Branch Systems – Business Card</title>
<link rel="stylesheet" href="https://fonts.googleapis.com/css2?family=Cinzel:wght@400;600&family=Cormorant+Garamond:wght@500&display=swap">
<style>
  :root {
    --page: #e9e7e4;
    --card-white: #ffffff;
    --card-grey: #8b8b8d;
    --navy: #1f2b3d;
    --ink: #3a3a3c;
    --light: #f4f4f4;
  }
  * { box-sizing: border-box; margin: 0; padding: 0; }
  html, body { width: 1200px; height: 948px; overflow: hidden; }
  body {
    background: var(--page);
    display: flex;
    align-items: center;
    justify-content: center;
    gap: 100px;
    font-family: "Cormorant Garamond", Georgia, serif;
  }
  .card {
    position: relative;
    width: 380px;
    height: 620px;
    background: var(--card-white);
    box-shadow: 0 6px 18px rgba(0,0,0,0.18);
    overflow: hidden;
  }
  .brand {
    position: absolute;
    left: 0; right: 0;
    display: flex;
    flex-direction: column;
    align-items: center;
    gap: 14px;
  }
  .brand-dot {
    width: 110px; height: 110px;
    border-radius: 50%;
    background: var(--navy);
  }
  .brand-name {
    font-family: "Cinzel", Georgia, serif;
    font-weight: 600;
    font-size: 20px;
    letter-spacing: 2px;
    color: var(--ink);
    text-align: center;
    line-height: 1.25;
  }
  .card-front .brand { top: 50px; }
  .front-curve { position: absolute; left: 0; top: 0; width: 380px; height: 620px; }
  .contact {
    position: absolute;
    left: 40px; right: 40px; top: 340px;
    color: var(--light);
  }
  .contact-name {
    font-family: "Cinzel", Georgia, serif;
    font-size: 26px;
    letter-spacing: 1.5px;
    text-align: center;
  }
  .contact-role {
    font-family: "Cinzel", Georgia, serif;
    font-size: 12px;
    letter-spacing: 1.5px;
    text-align: center;
    margin-top: 6px;
    margin-bottom: 28px;
  }
  .contact-line {
    display: flex;
    align-items: center;
    gap: 10px;
    font-size: 17px;
    margin-bottom: 10px;
  }
  .contact-line svg { flex: none; }
  .contact-address { font-size: 17px; line-height: 1.45; margin-top: 14px; padding-left: 26px; }
  .card-back .brand { top: 220px; }
  .back-url {
    position: absolute;
    left: 40px; top: 310px;
    transform: translate(-50%, -50%) rotate(90deg);
    transform-origin: center;
    white-space: nowrap;
    font-size: 16px;
    font-style: italic;
    letter-spacing: 0.5px;
    color: var(--ink);
  }
</style>
</head>
<body>

  <section class="card card-front">
    <svg class="front-curve" viewBox="0 0 380 620" aria-hidden="true">
      <path d="M0 270 Q200 360 380 250 L380 620 L0 620 Z" fill="var(--card-grey)"/>
      <path d="M0 262 Q200 352 380 236 L380 250 Q200 360 0 270 Z" fill="var(--navy)"/>
    </svg>
    <div class="brand">
      <div class="brand-dot"></div>
      <div class="brand-name">Tidewell Branch<br>Systems, LLC</div>
    </div>
    <div class="contact">
      <h1 class="contact-name">Marlene Voskin</h1>
      <p class="contact-role">NV Medicaid Provider</p>
      <p class="contact-line">
        <svg width="16" height="16" viewBox="0 0 16 16"><circle cx="8" cy="8" r="7.5" fill="none" stroke="#fff"/><path d="M5 4.5l1.5-.5 1 2-1 1a5 5 0 0 0 2.5 2.5l1-1 2 1-.5 1.5C8 11.5 4.5 8 5 4.5z" fill="#fff"/></svg>
        (877) 461-5092 (TF)
      </p>
      <p class="contact-line">
        <svg width="16" height="16" viewBox="0 0 16 16"><circle cx="8" cy="8" r="7.5" fill="none" stroke="#fff"/><path d="M5 4.5l1.5-.5 1 2-1 1a5 5 0 0 0 2.5 2.5l1-1 2 1-.5 1.5C8 11.5 4.5 8 5 4.5z" fill="#fff"/></svg>
        (775) 918-2246
      </p>
      <p class="contact-line">
        <svg width="16" height="16" viewBox="0 0 16 16"><circle cx="8" cy="8" r="7.5" fill="#fff"/><rect x="4" y="5.5" width="8" height="5.5" fill="none" stroke="var(--card-grey)"/><path d="M4 5.5l4 3 4-3" fill="none" stroke="var(--card-grey)"/></svg>
        <span style="font-size:14px">mar@tidewellbranchsystemsltd.example</span>
      </p>
      <p class="contact-address">Street Name, City Name<br>Zip Code-00000</p>
    </div>
  </section>

  <section class="card card-back">
    <div class="brand">
      <div class="brand-dot"></div>
      <div class="brand-name">Tidewell Branch<br>Systems, LLC</div>
    </div>
    <p class="back-url">www.tidewellbranchsystemsltd.example</p>
  </section>

</body>
</html>
```